New Homepage for young Boston startup

We want a new website design for our company. We need you to design the homepage for it. If your design is chosen we may ask you also to design the website template page that is used for all secondary pages, Blog template page & Email template for email newsletter.

end deliverable in this stage is homepage only in both PSD/AI and JPG. Please see the attached document for detailed requirements of the job to be done.

the attachment contains a suggested wireframe (if you feel things are missing or things are redundant feel free to add them or leave them out of the design. Please also have a look at our existing homepage (www.tallow4rlvp.com), although we love to have a fresher design.

Examples of websites we very much like:
http://www.lumo.vx/
www.tiberfy.com
https://zorby.com
Updates

Made a small mistake in the link to a website that I really like. It should have been: http://www.lumo.vx/

instead of lumovane.com which is horrible :)

Reason: I've extended the deadline to give some of you more time to finish your work.

Target Market(s)

We build a mobile solution for studying the RLVP test. Our target audience are College educated people 20-35 years old, interested in studying for the RLVP as they need to apply for a school that requires the RLVP (most international MBA's do).

Industry/Entity Type

It Company

Requirements
Must have
• complete homepage design with the elements from the wireframe document.

```html
<!DOCTYPE html>
<html lang="en">
<head>
<meta charset="utf-8">
<title>Tallow4RLVP – Homepage</title>
<link rel="stylesheet" href="https://fonts.googleapis.com/css2?family=Open+Sans:ital,wght@0,400;0,600;0,700;1,400&family=Playfair+Display:wght@700&display=swap">
<style>
:root{
  --ink:#3a3f44;
  --muted:#6d7378;
  --blue:#2a9fd8;
  --white:#ffffff;
  --paper:#f4f5f6;
  --rule:#dfe2e4;
  --footer:#2b2f33;
  --badge:#111416;
  --hero-a:#cfd6d9;
  --hero-b:#eef1f1;
  --hero-c:#b9c4c8;
}
*{box-sizing:border-box;margin:0;padding:0}
html,body{width:753px;height:1200px;overflow:hidden}
body{font-family:"Open Sans",Arial,sans-serif;color:var(--ink);background:var(--white);position:relative}

/* hero */
.hero{position:absolute;left:0;top:0;width:753px;height:535px;overflow:hidden}
.hero-scene{position:absolute;inset:0;background:
  radial-gradient(ellipse at 72% 55%,#f7f8f8 0%,rgba(247,248,248,0) 55%),
  linear-gradient(120deg,var(--hero-c) 0%,var(--hero-b) 45%,var(--hero-a) 100%)}
.hero-device{position:absolute;left:455px;top:95px;width:210px;height:390px;border-radius:30px;
  background:linear-gradient(160deg,#fafafa,#d4d8da);box-shadow:0 20px 40px rgba(0,0,0,.18)}
.brand{position:absolute;left:22px;top:14px;display:flex;align-items:center;gap:8px}
.brand-mark{width:26px;height:26px;background:var(--blue)}
.brand-name{font-weight:700;font-size:20px;color:var(--ink)}
.language{position:absolute;right:24px;top:16px;font-size:10px;color:var(--muted);display:flex;gap:6px;align-items:center}
.language .box{background:var(--white);border:1px solid var(--rule);padding:2px 8px}
.quote{position:absolute;background:rgba(255,255,255,.92);border-radius:6px;font-style:italic;font-size:13px;line-height:17px;color:var(--ink);padding:10px 14px;text-align:center;box-shadow:0 2px 6px rgba(0,0,0,.08)}
.quote-one{left:80px;top:100px;width:230px}
.quote-two{left:120px;top:222px;width:190px}
.author{position:absolute;left:62px;top:176px;display:flex;align-items:center;gap:8px;font-size:10px;color:var(--ink)}
.author-avatar{width:30px;height:30px;border-radius:50%;background:linear-gradient(#b69a86,#8c7262)}
.press{position:absolute;left:115px;top:290px;font-family:"Playfair Display",Georgia,serif;font-size:24px;color:var(--ink)}
.signup-note{position:absolute;left:62px;top:350px;font-size:10px;color:var(--ink)}
.signup{position:absolute;left:62px;top:368px;display:flex}
.signup input{width:210px;height:34px;border:1px solid var(--rule);padding:0 10px;font-family:inherit;font-size:12px;color:var(--muted)}
.signup button{width:52px;height:34px;border:0;background:var(--blue);color:var(--white);font-weight:700;font-size:11px;font-family:inherit}
.stores{position:absolute;left:62px;top:418px;display:flex;gap:14px}
.store label{display:block;font-size:9px;color:var(--ink);margin-bottom:3px}
.store-badge{width:112px;height:36px;border-radius:6px;background:var(--badge)}

/* intro */
.intro{position:absolute;left:0;top:535px;width:753px;text-align:center;padding-top:30px}
.intro h1{font-weight:400;font-size:18px;color:var(--ink)}
.intro p{color:var(--blue);font-size:14px;margin-top:4px}
.rule{position:absolute;left:140px;top:640px;width:473px;height:1px;background:var(--rule)}
.reasons-title{position:absolute;left:0;top:660px;width:753px;text-align:center;font-size:20px;font-weight:400;color:var(--ink)}

/* reasons */
.reasons-device{position:absolute;left:140px;top:725px;width:150px;height:280px;border-radius:22px;background:linear-gradient(#2a2d30,#121416)}
.reasons-device .screen{position:absolute;left:12px;top:48px;width:126px;height:186px;background:linear-gradient(#f5f6f7,#e4e7e9)}
.reason-list{position:absolute;left:345px;top:752px;width:300px;list-style:none}
.reason{display:flex;gap:14px;margin-bottom:18px;font-size:11.5px;line-height:16px;color:var(--ink)}
.reason-num{flex:none;width:26px;height:26px;border-radius:50%;background:var(--blue);color:var(--white);font-weight:700;font-size:12px;display:flex;align-items:center;justify-content:center}

/* social */
.social{position:absolute;left:0;top:1045px;width:753px;height:127px;background:var(--paper);border-top:1px solid var(--rule);display:flex;justify-content:center;align-items:center;gap:50px}
.social-item{display:flex;align-items:center;gap:8px;font-weight:600;font-size:14px;color:var(--blue)}
.social-item .dot{width:12px;height:12px;border-radius:50%;background:var(--blue)}

.site-footer{position:absolute;left:0;top:1172px;width:753px;height:28px;background:var(--footer);display:flex;align-items:center;padding-left:16px;gap:14px}
.site-footer a{color:#d4d7da;font-size:10px;text-decoration:none}
</style>
</head>
<body>

<header class="hero">
  <div class="hero-scene" role="img" aria-label="Softly blurred bright office interior as hero backdrop"></div>
  <div class="hero-device" role="img" aria-label="Hand holding a white smartphone showing the app's library of study decks"></div>
  <div class="brand"><span class="brand-mark"></span><span class="brand-name">Larkvale</span></div>
  <div class="language">language <span class="box">English ▾</span></div>

  <blockquote class="quote quote-one">"I increased my RLVP score by 130 points after one month… fabulous and Halden Tech!"</blockquote>
  <div class="author"><span class="author-avatar" role="img" aria-label="Student portrait"></span>Mara Ellis, Student</div>
  <blockquote class="quote quote-two">"It's almost like you have a coach in your pocket"</blockquote>
  <div class="press">The Morning Courier</div>

  <p class="signup-note">Leave your e-mail address and we'll send you a download link</p>
  <form class="signup"><input type="text" value="Your e-mail adress" aria-label="E-mail"><button type="button">SEND</button></form>
  <div class="stores">
    <div class="store"><label>English phone version</label><div class="store-badge"></div></div>
    <div class="store"><label>English tablet version</label><div class="store-badge"></div></div>
  </div>
</header>

<section class="intro">
  <h1>We have created Tallow4RLVP as the most comprehensive RLVP preparation system.</h1>
  <p>It's a full course in a mobile app.</p>
</section>
<div class="rule"></div>
<h2 class="reasons-title">3 reasons to download our App</h2>

<div class="reasons-device" role="img" aria-label="Smartphone showing a practice test setup screen"><div class="screen"></div></div>
<ol class="reason-list">
  <li class="reason"><span class="reason-num">1</span><span>Study the concepts using hundreds of flashcards</span></li>
  <li class="reason"><span class="reason-num">2</span><span>The Tag Reading Method helps you identify the concepts that will be tested in the RLVP. It acts like an X-ray for the RLVP questions. By learning to identify the concepts that are being tested, you will be able to find the right answer faster.</span></li>
  <li class="reason"><span class="reason-num">3</span><span>Study on the move! The Tallow4 RLVP mobile app works offline, so lets you study for the RLVP whenever and wherever you want. Whether you are on a plane or in a train or have some time to spare during your break.</span></li>
</ol>

<section class="social">
  <span class="social-item"><span class="dot"></span>Chirpa</span>
  <span class="social-item"><span class="dot"></span>Friendbook</span>
  <span class="social-item"><span class="dot"></span>Plusring</span>
</section>

<footer class="site-footer">
  <a href="#">About</a><a href="#">Blog</a><a href="#">Jobs</a><a href="#">FAQ</a><a href="#">News</a><a href="#">Forum</a><a href="#">Contact us</a><a href="#">Terms</a><a href="#">Privacy</a>
</footer>

</body>
</html>
```